Business Card Design needed - Something Awesome!

Need a business card designed. Company is "Harbor Vane Consulting" we do consulting and also have sales automation technology.
I'm going to use thick stock or metal, something really nice... I was thinking about a QR Code on the back that would just upload my contact info to the persons contact, etc -

This is a Strategy Company with a tech feel. I'm open to ideas but really want this to be nice!

I need a template that should include:

Name | Position or Title
D: 555.203.8146
www.harborvaneconsulting.example

I'm going to attach my contact so you can use that one, I need to get this printed.

Target Market(s)

Small to mid size customers, Entrepreneurs etc.

Industry/Entity Type

Consulting, Tech, Private Equity.

Contact Information for Business Card

Name, Phone, Maybe email, URL

Font styles to use
Sans Serif

Colors

Designer to choose only greyscale colors for use in the design.

Requirements
Must have
• Fresh, Clean, stand out from the crowd - will be on thick stock or metal.
Nice to have
• Clean, simple yet impactful.
Should not have
• Not cartoonish

```html
<!DOCTYPE html>
<html lang="en">
<head>
<meta charset="utf-8">
<title>Harbor Vane Consulting — Business Card</title>
<link rel="stylesheet" href="https://fonts.googleapis.com/css2?family=Arimo:wght@400;700&display=swap">
<style>
  :root {
    --backdrop: #3a3a3a;
    --card: #0c0c0c;
    --silver: #c9c9c9;
    --silver-bright: #e6e6e6;
    --text-muted: #a8a8a8;
    --rule: #555555;
  }
  * { margin: 0; padding: 0; box-sizing: border-box; }
  html, body {
    width: 1200px;
    height: 801px;
    overflow: hidden;
    background: var(--backdrop);
    font-family: "Arimo", Arial, sans-serif;
  }
  .stage {
    position: relative;
    width: 1200px;
    height: 801px;
    display: flex;
    align-items: center;
    justify-content: center;
    gap: 40px;
  }
  .card {
    width: 520px;
    height: 297px;
    background: var(--card);
    position: relative;
    box-shadow: 0 10px 24px rgba(0,0,0,0.35);
  }

  /* Front: wordmark + contact details */
  .card--front {
    display: flex;
    align-items: center;
    padding: 0 34px 0 40px;
  }
  .wordmark {
    display: flex;
    align-items: center;
    gap: 8px;
    color: var(--silver);
    font-weight: 400;
    letter-spacing: 0.02em;
    white-space: nowrap;
  }
  .wordmark__square {
    width: 12px;
    height: 12px;
    background: var(--silver-bright);
    flex: none;
  }
  .card--front .wordmark { font-size: 26px; }
  .divider {
    width: 1px;
    height: 118px;
    background: var(--rule);
    margin: 0 20px 0 22px;
    flex: none;
  }
  .contact { color: var(--text-muted); font-size: 11.5px; line-height: 1.45; }
  .contact__name {
    color: var(--silver-bright);
    font-weight: 700;
    font-size: 15px;
    letter-spacing: 0.03em;
    text-transform: uppercase;
  }
  .contact__title { font-size: 12px; margin-bottom: 12px; }
  .contact__line { display: flex; align-items: center; gap: 7px; }
  .contact__icon { width: 10px; height: 10px; flex: none; }

  /* Back: large wordmark */
  .card--back {
    display: flex;
    align-items: center;
    justify-content: center;
  }
  .card--back .wordmark { font-size: 46px; gap: 14px; }
  .card--back .wordmark__square { width: 22px; height: 22px; }
</style>
</head>
<body>
<main class="stage">
  <section class="card card--front" aria-label="Card front">
    <div class="wordmark">
      <span class="wordmark__square"></span>
      <span class="wordmark__name">HARBOR VANE</span>
    </div>
    <div class="divider"></div>
    <div class="contact">
      <p class="contact__name">Dorian K. Vale</p>
      <p class="contact__title">Founder / CEO</p>
      <p class="contact__line">
        <svg class="contact__icon" viewBox="0 0 10 10" aria-hidden="true"><circle cx="5" cy="5" r="5" fill="#a8a8a8"/><path d="M3 2.5 L4.2 2.5 L4.6 4 L3.9 4.5 Q4.5 5.8 5.6 6.2 L6.1 5.5 L7.5 5.9 L7.5 7.1 Q4 7.4 3 2.5Z" fill="#0c0c0c"/></svg>
        555.203.8146
      </p>
      <p class="contact__line">
        <svg class="contact__icon" viewBox="0 0 10 10" aria-hidden="true"><circle cx="5" cy="5" r="5" fill="#a8a8a8"/><rect x="2.4" y="3.2" width="5.2" height="3.6" fill="#0c0c0c"/><path d="M2.6 3.4 L5 5.2 L7.4 3.4" stroke="#a8a8a8" stroke-width="0.6" fill="none"/></svg>
        info@harborvaneconsulting.example
      </p>
      <p class="contact__line">
        <svg class="contact__icon" viewBox="0 0 10 10" aria-hidden="true"><circle cx="5" cy="5" r="5" fill="#a8a8a8"/><circle cx="5" cy="5" r="2.8" fill="none" stroke="#0c0c0c" stroke-width="0.7"/><path d="M2.2 5 H7.8 M5 2.2 V7.8" stroke="#0c0c0c" stroke-width="0.6"/></svg>
        www.harborvaneconsulting.example
      </p>
    </div>
  </section>

  <section class="card card--back" aria-label="Card back">
    <div class="wordmark">
      <span class="wordmark__square"></span>
      <span class="wordmark__name">HARBOR VANE</span>
    </div>
  </section>
</main>
</body>
</html>
```